Vera-Shine Janitorial Services

Looking for a modern design for my new business. I like the clear see through of the card I've attached. The business is built around The Pellmar Apex 720 system, with that said I'd like to add the pellmar logo on the bachside with the statement of Powered by (then the Pellmar Logo). I really like the layout and color schemes of the card I attached. Black, Blue, and White. I would like to incorporate three images into the diamond shape, as seem in the layout.

Gordon Pike
Managing Partner

Still waiting on revisions?

```html
<!DOCTYPE html>
<html lang="en">
<head>
<meta charset="utf-8">
<title>Vera-Shine Services – Business Card</title>
<link rel="stylesheet" href="https://fonts.googleapis.com/css2?family=Cantarell&family=Roboto:wght@400;500;700&display=swap">
<style>
  :root {
    --stage: #e9e6e1;
    --ink-dark: #1b1918;
    --frost: #d8d1c7;
    --frost-edge: #c2b8ab;
    --blue-line: #1c80b3;
    --blue-deep: #1d4e7a;
    --teal: #1f8fae;
    --sky: #58b9e6;
    --white: #ffffff;
    --badge: #caa29f;
  }
  * { box-sizing: border-box; margin: 0; padding: 0; }
  html, body { width: 1200px; height: 615px; overflow: hidden; background: var(--stage); }
  .stage { position: relative; width: 1200px; height: 615px; }
  .card {
    position: absolute; top: 153px; width: 540px; height: 309px;
    border-radius: 12px; overflow: hidden;
    box-shadow: 0 6px 18px rgba(0,0,0,.18);
  }
  .card--front { left: 40px; }
  .card--back { left: 620px; }
  .card__art { position: absolute; inset: 0; width: 540px; height: 309px; }
  .brand { position: absolute; color: var(--white); font-family: "Cantarell", sans-serif; text-align: center; line-height: 1; }
  .brand__name { font-size: 30px; letter-spacing: .5px; }
  .brand__tag { font-size: 16px; letter-spacing: 1.5px; margin-top: 2px; }
  .card--front .brand { left: 18px; top: 140px; width: 180px; }
  .card--back .brand { left: 348px; top: 140px; width: 180px; }
  .powered { position: absolute; left: 27px; top: 212px; font-family: "Roboto", sans-serif; color: var(--white); }
  .powered__label { font-size: 15px; font-weight: 500; }
  .powered__partner { margin-top: 14px; font-size: 22px; font-weight: 500; }
  .holder { position: absolute; left: 398px; top: 256px; font-family: "Roboto", sans-serif; text-align: right; width: 128px; }
  .holder__name { color: var(--blue-deep); font-size: 17px; font-weight: 700; letter-spacing: .3px; }
  .holder__role { color: var(--teal); font-size: 13px; margin-top: 2px; }
  .contacts { position: absolute; right: 14px; top: 201px; list-style: none; font-family: "Roboto", sans-serif; color: var(--white); font-size: 11.5px; text-align: right; }
  .contacts li { display: flex; justify-content: flex-end; align-items: center; gap: 7px; height: 17px; }
  .contacts svg { width: 11px; height: 11px; flex: none; }
</style>
</head>
<body>
<main class="stage">

  <!-- Front side -->
  <section class="card card--front" aria-label="Card front">
    <svg class="card__art" viewBox="0 0 540 309" aria-hidden="false">
      <defs>
        <linearGradient id="frostFront" x1="0" y1="0" x2="1" y2="1">
          <stop offset="0" stop-color="#e2dbd1"/><stop offset="1" stop-color="#c9bfb2"/>
        </linearGradient>
        <linearGradient id="photoA" x1="0" y1="0" x2="1" y2="1">
          <stop offset="0" stop-color="#5f6163"/><stop offset="1" stop-color="#b9b4ac"/>
        </linearGradient>
        <linearGradient id="photoB" x1="0" y1="0" x2="1" y2="1">
          <stop offset="0" stop-color="#7d8a90"/><stop offset="1" stop-color="#c8c1b4"/>
        </linearGradient>
        <linearGradient id="photoC" x1="0" y1="0" x2="1" y2="1">
          <stop offset="0" stop-color="#8e8a80"/><stop offset="1" stop-color="#5a8f98"/>
        </linearGradient>
        <linearGradient id="dotsFill" x1="0" y1="0" x2="1" y2="1">
          <stop offset="0" stop-color="#2e8fc4"/><stop offset="1" stop-color="#1c5f93"/>
        </linearGradient>
      </defs>
      <rect class="card__frost" width="540" height="309" fill="url(#frostFront)"/>
      <polygon class="card__dark" points="0,0 352,0 476,126 340,262 387,309 0,309" fill="var(--ink-dark)"/>
      <polygon class="card__dots" role="img" aria-label="Scattered blue bubble pattern" points="392,0 540,0 540,118 500,150 440,50" fill="url(#dotsFill)" opacity=".75"/>
      <polygon class="diamond diamond--large" role="img" aria-label="Photo: technician operating a disinfecting sprayer" points="372,20 470,118 372,216 274,118" fill="url(#photoA)" stroke="var(--blue-line)" stroke-width="2.5"/>
      <polygon class="diamond diamond--left" role="img" aria-label="Photo: sprayer cart with supply tanks" points="258,98 320,160 258,222 196,160" fill="url(#photoB)" stroke="var(--blue-line)" stroke-width="2.5"/>
      <polygon class="diamond diamond--bottom" role="img" aria-label="Photo: freshly cleaned room interior" points="329,180 393,244 329,308 265,244" fill="url(#photoC)" stroke="var(--blue-line)" stroke-width="2.5"/>
      <circle class="brand__mark" cx="104" cy="74" r="50" fill="none" stroke="var(--sky)" stroke-width="3"/>
      <circle class="partner__badge" cx="238" cy="262" r="30" fill="var(--badge)"/>
    </svg>
    <div class="brand">
      <div class="brand__name">Vera-Shine</div>
      <div class="brand__tag">Services</div>
    </div>
    <div class="powered">
      <div class="powered__label">Powered by</div>
      <div class="powered__partner">Pellmar</div>
    </div>
    <div class="holder">
      <div class="holder__name">GORDON PIKE</div>
      <div class="holder__role">Managing Partner</div>
    </div>
  </section>

  <!-- Back side -->
  <section class="card card--back" aria-label="Card back">
    <svg class="card__art" viewBox="0 0 540 309">
      <defs>
        <linearGradient id="frostBack" x1="1" y1="0" x2="0" y2="1">
          <stop offset="0" stop-color="#e2dbd1"/><stop offset="1" stop-color="#c9bfb2"/>
        </linearGradient>
        <linearGradient id="photoA2" x1="1" y1="0" x2="0" y2="1">
          <stop offset="0" stop-color="#5f6163"/><stop offset="1" stop-color="#b9b4ac"/>
        </linearGradient>
        <linearGradient id="photoB2" x1="1" y1="0" x2="0" y2="1">
          <stop offset="0" stop-color="#7d8a90"/><stop offset="1" stop-color="#c8c1b4"/>
        </linearGradient>
        <linearGradient id="photoC2" x1="1" y1="0" x2="0" y2="1">
          <stop offset="0" stop-color="#8e8a80"/><stop offset="1" stop-color="#5a8f98"/>
        </linearGradient>
        <linearGradient id="dotsFill2" x1="1" y1="0" x2="0" y2="1">
          <stop offset="0" stop-color="#2e8fc4"/><stop offset="1" stop-color="#1c5f93"/>
        </linearGradient>
      </defs>
      <rect class="card__frost" width="540" height="309" fill="url(#frostBack)"/>
      <polygon class="card__dark" points="540,0 188,0 64,126 200,262 153,309 540,309" fill="var(--ink-dark)"/>
      <polygon class="card__dots" role="img" aria-label="Scattered blue bubble pattern" points="148,0 0,0 0,118 40,150 100,50" fill="url(#dotsFill2)" opacity=".75"/>
      <polygon class="diamond diamond--large" role="img" aria-label="Photo: technician operating a disinfecting sprayer" points="168,20 266,118 168,216 70,118" fill="url(#photoA2)" stroke="var(--blue-line)" stroke-width="2.5"/>
      <polygon class="diamond diamond--right" role="img" aria-label="Photo: sprayer cart with supply tanks" points="282,98 344,160 282,222 220,160" fill="url(#photoB2)" stroke="var(--blue-line)" stroke-width="2.5"/>
      <polygon class="diamond diamond--bottom" role="img" aria-label="Photo: freshly cleaned room interior" points="211,180 275,244 211,308 147,244" fill="url(#photoC2)" stroke="var(--blue-line)" stroke-width="2.5"/>
      <circle class="brand__mark" cx="438" cy="74" r="50" fill="none" stroke="var(--sky)" stroke-width="3"/>
    </svg>
    <div class="brand">
      <div class="brand__name">Vera-Shine</div>
      <div class="brand__tag">Services</div>
    </div>
    <ul class="contacts">
      <li>(555)201-4480
        <svg viewBox="0 0 12 12" aria-hidden="true"><path d="M2.5 1l2 2.2-1 1.3a7 7 0 0 0 4 4l1.3-1 2.2 2-1.3 1.5C5.5 11 1 6.5 1 2.3z" fill="var(--sky)"/></svg></li>
      <li>(555)201-4481
        <svg viewBox="0 0 12 12" aria-hidden="true"><rect x="3" y=".8" width="6" height="10.4" rx="1" fill="none" stroke="var(--sky)" stroke-width="1.4"/></svg></li>
      <li>gordon@verashine-services.com
        <svg viewBox="0 0 12 12" aria-hidden="true"><rect x=".8" y="2.5" width="10.4" height="7" fill="var(--sky)"/><path d="M1 3l5 3.5L11 3" fill="none" stroke="var(--ink-dark)" stroke-width="1"/></svg></li>
      <li>www.verashine-services.com
        <svg viewBox="0 0 12 12" aria-hidden="true"><circle cx="6" cy="6" r="5" fill="none" stroke="var(--sky)" stroke-width="1.4"/><path d="M1 6h10M6 1c2.5 3 2.5 7 0 10M6 1c-2.5 3-2.5 7 0 10" fill="none" stroke="var(--sky)" stroke-width="1"/></svg></li>
      <li>P.O. Box 4410, Palm Ridge, CA 92299
        <svg viewBox="0 0 12 12" aria-hidden="true"><path d="M6 11.5S2 7 2 4.5a4 4 0 0 1 8 0C10 7 6 11.5 6 11.5z" fill="var(--sky)"/><circle cx="6" cy="4.5" r="1.5" fill="var(--ink-dark)"/></svg></li>
    </ul>
  </section>

</main>
</body>
</html>
```